Update New Business Card - For Start Up

I need to update my business card, I have our old version for example. I would like to keep to the same colors and theme. We are a threat reporting and case management tool for corporations and educational institutions.

Target Market(s)

Corporate Security and Human Resources, School Administrators and Superintendents.

Industry/Entity Type

Physical Security and Technology.

Contact Information for Business Card

My Name, Founder/CEO, phone number 555-214-6082, Logo, Web...

Colors
0054AA
0677BA
7BADD7
CADEEF
E8F1F8

Requirements
Must have
• Something new and trendy.

```html
<!DOCTYPE html>
<html lang="en">
<head>
<meta charset="utf-8">
<title>Varnoquell Business Card</title>
<link rel="stylesheet" href="https://fonts.googleapis.com/css2?family=Poppins:wght@400;500;700&display=swap">
<style>
  :root {
    --navy-deep: #0b1a44;
    --navy: #143a8a;
    --royal: #1a4ea8;
    --brand-blue: #1b78bf;
    --accent-blue: #0054aa;
    --sky: #7badd7;
    --ink: #1c1c1c;
    --paper: #ffffff;
    --stage: #e6e6e6;
  }
  * { margin: 0; padding: 0; box-sizing: border-box; }
  html, body { width: 1200px; height: 1017px; overflow: hidden; }
  body {
    background: var(--stage);
    font-family: "Poppins", sans-serif;
    position: relative;
  }
  .card {
    position: absolute;
    width: 700px;
    height: 400px;
    overflow: hidden;
    box-shadow: 0 8px 24px rgba(0,0,0,0.18);
  }
  /* Front */
  .card-front {
    left: 40px; top: 40px;
    background: linear-gradient(135deg, var(--navy-deep) 0%, var(--navy) 55%, var(--royal) 100%);
    color: var(--paper);
  }
  .radar-area {
    position: absolute;
    left: -60px; top: 40px;
    width: 380px; height: 380px;
    border-radius: 50%;
    background: radial-gradient(circle, rgba(60,110,190,0.45) 0%, rgba(20,50,120,0.35) 55%, rgba(11,26,68,0) 72%);
  }
  .front-brand {
    position: absolute;
    left: 130px; top: 150px;
    display: flex; align-items: center; gap: 18px;
  }
  .brand-dot {
    width: 78px; height: 78px; border-radius: 50%;
    background: var(--paper);
    flex: none;
  }
  .brand-name {
    font-weight: 500;
    font-size: 50px;
    letter-spacing: 7px;
    color: var(--paper);
    white-space: nowrap;
  }
  .front-web {
    position: absolute;
    left: 240px; top: 250px;
    font-size: 17px;
    letter-spacing: 5px;
    font-weight: 500;
    white-space: nowrap;
  }
  .circuit { position: absolute; left: 0; top: 0; }
  /* Back */
  .card-back {
    left: 460px; top: 577px;
    background: var(--paper);
  }
  .mark-panel {
    position: absolute;
    right: -80px; top: -120px;
    width: 420px; height: 420px;
    border-radius: 50%;
    background: var(--brand-blue);
  }
  .person-name {
    position: absolute;
    left: 48px; top: 110px;
    font-weight: 700;
    font-size: 42px;
    color: var(--brand-blue);
    line-height: 1;
  }
  .person-title {
    position: absolute;
    left: 50px; top: 160px;
    font-size: 18px;
    color: var(--ink);
  }
  .contact-icons {
    position: absolute;
    left: 150px; top: 250px;
    display: flex; gap: 12px;
  }
  .contact-icons svg { width: 30px; height: 30px; }
  .contact-list {
    position: absolute;
    left: 150px; top: 292px;
    list-style: none;
    font-size: 18px;
    color: var(--ink);
    line-height: 1.45;
  }
  .contact-web { letter-spacing: 4px; }
</style>
</head>
<body>

<section class="card card-front">
  <div class="radar-area" role="img" aria-label="Radar sweep illustration in dark blue tones"></div>
  <svg class="circuit" width="700" height="400" viewBox="0 0 700 400">
    <g fill="none" stroke="#ffffff" stroke-width="2">
      <polyline points="40,370 290,370 300,358"/>
      <polyline points="590,246 604,260 700,260"/>
    </g>
    <circle cx="300" cy="358" r="5" fill="#ffffff"/>
    <circle cx="590" cy="246" r="5" fill="#ffffff"/>
  </svg>
  <div class="front-brand">
    <span class="brand-dot"></span>
    <span class="brand-name">VARNOQUELL</span>
  </div>
  <div class="front-web">WWW.VARNOQUELL.CO</div>
</section>

<section class="card card-back">
  <div class="mark-panel" role="img" aria-label="Large brand blue decorative shape"></div>
  <h1 class="person-name">Alex Marlow</h1>
  <p class="person-title">Founder/CEO</p>
  <svg class="circuit" width="700" height="400" viewBox="0 0 700 400">
    <polyline points="420,200 115,200 110,230" fill="none" stroke="#1b78bf" stroke-width="3"/>
    <circle cx="110" cy="232" r="6" fill="#1b78bf"/>
  </svg>
  <div class="contact-icons">
    <svg viewBox="0 0 30 30" aria-label="Phone">
      <circle cx="15" cy="15" r="15" fill="#1b78bf"/>
      <path d="M10 8 l3 0 l1 4 l-2 1.5 a8 8 0 0 0 4.5 4.5 l1.5 -2 l4 1 l0 3 a2 2 0 0 1 -2 2 a13 13 0 0 1 -12 -12 a2 2 0 0 1 2 -2z" fill="#fff"/>
    </svg>
    <svg viewBox="0 0 30 30" aria-label="Email">
      <circle cx="15" cy="15" r="15" fill="#1b78bf"/>
      <rect x="8" y="10" width="14" height="10" fill="#fff"/>
      <polyline points="8,10 15,16 22,10" fill="none" stroke="#1b78bf" stroke-width="1.5"/>
    </svg>
    <svg viewBox="0 0 30 30" aria-label="Website">
      <circle cx="15" cy="15" r="15" fill="#1b78bf"/>
      <g fill="none" stroke="#fff" stroke-width="1.4">
        <circle cx="15" cy="15" r="7"/>
        <ellipse cx="15" cy="15" rx="3" ry="7"/>
        <line x1="8" y1="15" x2="22" y2="15"/>
      </g>
    </svg>
  </div>
  <ul class="contact-list">
    <li>555-214-6082</li>
    <li>alex@varnoquell.co</li>
    <li class="contact-web">WWW.VARNOQUELL.CO</li>
  </ul>
</section>

</body>
</html>
```